Nutritionist and Personal Chef Services Flyer. My style is clean and contemporary.

I'm looking for a clean and stylish flyer that may or may not list my services and/or prices. These flyers will be featured in southern california (orange county and los angeles) fitness centers, wellness clinics, doctors offices, restaurants etc. so it has to be appropriate for any kind of facility. I want the concept design to be similar to my website:

www.verdanttablewellness.com

This is very important! Also, please see attached file to see what my header and business cards look like to keep style and formatting consistent.
Thanks so much!

The dimensions are going to be 5.5" by 8.5" vertical. I'd like it to be double-sided with a picture on one side and my information on the other side. For the photo side, I like the idea of having the picture of the hands and cutting board (fine for this to run horizontal). On the information side I need it to address the following:

1. I'd like to have a small photo of myself. I will upload which photo I want.
2. I want my header with my font and the kiwi exactly as is. Please see attachment and keep that formatting exactly.
3. Specialty Services:
Sports Nutrition
Weight-loss
Anti-aging and Detoxification
Cancer Prevention, Management and Survivorship
Children's Health and Wellness
Specialty Diets

4. My contact info:
Marissa Okafor, C.N. NC
949-555-0184
verdanttablewellness@mailpost.example

5. My website and the FB logo

6. Call or email me today to schedule a free 30-minute consultation.

```html
<!DOCTYPE html>
<html lang="en">
<head>
<meta charset="utf-8">
<title>Verdant Table Wellness – Flyer</title>
<link rel="stylesheet" href="https://fonts.googleapis.com/css2?family=Roboto+Slab:wght@400;700&family=Source+Sans+3:wght@400;700&display=swap">
<style>
  :root {
    --green: #8cbb3c;
    --green-dark: #6f9a2a;
    --charcoal: #333333;
    --ink: #2a2a2a;
    --muted: #555555;
    --white: #ffffff;
    --backdrop: #ebeced;
  }
  * { box-sizing: border-box; margin: 0; padding: 0; }
  html, body { width: 1200px; height: 1000px; overflow: hidden; }
  body {
    background: var(--backdrop);
    font-family: "Source Sans 3", Arial, sans-serif;
    color: var(--ink);
    position: relative;
  }
  .flyer {
    position: absolute;
    top: 60px;
    width: 570px;
    height: 880px;
    background: var(--white);
    overflow: hidden;
    box-shadow: 0 2px 8px rgba(0,0,0,.12);
  }
  .flyer--info { left: 20px; }
  .flyer--photo { left: 610px; }
  .top-rule { height: 10px; background: var(--green); }

  /* brand header */
  .brand {
    display: flex;
    align-items: center;
    justify-content: center;
    gap: 18px;
    background: var(--white);
  }
  .brand__text { text-align: center; }
  .brand__name {
    font-family: "Roboto Slab", Georgia, serif;
    font-weight: 400;
    font-size: 25px;
    letter-spacing: 1.5px;
    text-transform: uppercase;
    color: var(--ink);
  }
  .brand__tagline {
    font-family: "Roboto Slab", Georgia, serif;
    font-size: 14px;
    color: var(--muted);
    margin-top: 4px;
  }
  .brand__dot {
    width: 48px; height: 48px;
    border-radius: 50%;
    background: var(--green);
    flex: none;
  }

  /* info side */
  .food-strip {
    height: 70px;
    background: linear-gradient(90deg, #f4f1ec 0%, #e2d9cf 40%, #d9513a 62%, #9cc25a 80%, #f1efe9 100%);
  }
  .flyer--info .brand { height: 120px; }
  .services {
    height: 250px;
    background: var(--green);
    color: var(--white);
    padding: 34px 40px 0 52px;
  }
  .services__title {
    font-family: "Roboto Slab", Georgia, serif;
    font-size: 26px;
    font-weight: 400;
    margin-bottom: 14px;
  }
  .services__list { list-style: none; }
  .services__item {
    display: flex; align-items: center; gap: 9px;
    font-size: 17px; line-height: 28px;
  }
  .services__item svg { width: 15px; height: 15px; flex: none; }
  .contact {
    height: 300px;
    display: flex;
    padding: 22px 40px 0 60px;
    gap: 34px;
  }
  .contact__portrait {
    width: 190px; height: 278px;
    background: linear-gradient(180deg, #8a5a3c 0%, #c99a7c 35%, #7fcbbd 60%, #e9e6e0 100%);
    border-radius: 4px;
  }
  .contact__details { padding-top: 6px; }
  .contact__name {
    font-family: "Roboto Slab", Georgia, serif;
    font-weight: 700;
    font-size: 19px;
  }
  .contact__name span { font-weight: 400; font-size: 16px; }
  .contact__row {
    display: flex; align-items: center; gap: 12px;
    margin-top: 20px;
    font-size: 15px;
  }
  .contact__row--small { font-size: 11.5px; }
  .contact__row svg { width: 18px; height: 18px; flex: none; }
  .contact__social {
    width: 30px; height: 30px; border-radius: 50%;
    background: var(--green);
    margin: 22px 0 0 88px;
  }
  .cta {
    height: 130px;
    background: var(--charcoal);
    color: var(--white);
    font-size: 22px;
    line-height: 30px;
    padding: 30px 60px 0 60px;
  }
  .cta strong { font-weight: 700; }

  /* photo side */
  .hero-photo {
    position: absolute; left: 0; top: 10px; width: 570px; height: 780px;
    background: linear-gradient(160deg, #f6f6f4 0%, #e6ece3 35%, #e5e3df 55%, #d8473a 68%, #c7a77d 82%, #f0efec 100%);
  }
  .flyer--photo .brand {
    position: absolute; left: 0; top: 60px; width: 570px; height: 130px;
  }
  .web-band {
    position: absolute; left: 0; bottom: 0; width: 570px; height: 90px;
    background: var(--green);
    color: var(--white);
    font-size: 23px;
    display: flex; align-items: center; justify-content: center;
    letter-spacing: .3px;
  }
</style>
</head>
<body>

<section class="flyer flyer--info">
  <div class="top-rule"></div>
  <div class="food-strip" role="img" aria-label="Photo of a glass bowl of fresh salad with tomatoes and cucumber"></div>
  <header class="brand">
    <div class="brand__text">
      <div class="brand__name">Verdant Table Wellness</div>
      <div class="brand__tagline">Nutrition Designs | Personal Chef Services</div>
    </div>
    <div class="brand__dot"></div>
  </header>

  <div class="services">
    <h2 class="services__title">Specialty Services:</h2>
    <ul class="services__list">
      <li class="services__item"><svg viewBox="0 0 16 16"><circle cx="8" cy="8" r="7" fill="none" stroke="#fff" stroke-width="1.5"/><path d="M4.8 8.2l2.2 2.1 4.2-4.4" fill="none" stroke="#fff" stroke-width="1.6"/></svg>Sports Nutrition</li>
      <li class="services__item"><svg viewBox="0 0 16 16"><circle cx="8" cy="8" r="7" fill="none" stroke="#fff" stroke-width="1.5"/><path d="M4.8 8.2l2.2 2.1 4.2-4.4" fill="none" stroke="#fff" stroke-width="1.6"/></svg>Weight-loss</li>
      <li class="services__item"><svg viewBox="0 0 16 16"><circle cx="8" cy="8" r="7" fill="none" stroke="#fff" stroke-width="1.5"/><path d="M4.8 8.2l2.2 2.1 4.2-4.4" fill="none" stroke="#fff" stroke-width="1.6"/></svg>Anti-aging and Detoxification</li>
      <li class="services__item"><svg viewBox="0 0 16 16"><circle cx="8" cy="8" r="7" fill="none" stroke="#fff" stroke-width="1.5"/><path d="M4.8 8.2l2.2 2.1 4.2-4.4" fill="none" stroke="#fff" stroke-width="1.6"/></svg>Cancer Prevention, Management and Survivorship</li>
      <li class="services__item"><svg viewBox="0 0 16 16"><circle cx="8" cy="8" r="7" fill="none" stroke="#fff" stroke-width="1.5"/><path d="M4.8 8.2l2.2 2.1 4.2-4.4" fill="none" stroke="#fff" stroke-width="1.6"/></svg>Children's Health and Wellness</li>
      <li class="services__item"><svg viewBox="0 0 16 16"><circle cx="8" cy="8" r="7" fill="none" stroke="#fff" stroke-width="1.5"/><path d="M4.8 8.2l2.2 2.1 4.2-4.4" fill="none" stroke="#fff" stroke-width="1.6"/></svg>Specialty Diets</li>
    </ul>
  </div>

  <div class="contact">
    <div class="contact__portrait" role="img" aria-label="Portrait photo of the nutritionist in a teal top and white apron"></div>
    <div class="contact__details">
      <div class="contact__name">Marissa Okafor, <span>C.N. NC</span></div>
      <div class="contact__row">
        <svg viewBox="0 0 18 18"><rect x="5" y="1" width="8" height="16" rx="1.5" fill="none" stroke="#8cbb3c" stroke-width="1.8"/><rect x="7" y="4" width="4" height="5" fill="#8cbb3c"/></svg>
        949-555-0184
      </div>
      <div class="contact__row contact__row--small">
        <svg viewBox="0 0 18 18"><rect x="1.5" y="4" width="15" height="10" fill="#8cbb3c"/><path d="M1.5 4l7.5 6 7.5-6" fill="none" stroke="#fff" stroke-width="1.4"/></svg>
        verdanttablewellness@mailpost.example
      </div>
      <div class="contact__row contact__row--small">
        <svg viewBox="0 0 18 18"><circle cx="9" cy="9" r="7.5" fill="#8cbb3c"/><path d="M1.5 9h15M9 1.5v15M3.5 5h11M3.5 13h11" stroke="#fff" stroke-width="1"/><ellipse cx="9" cy="9" rx="3.5" ry="7.5" fill="none" stroke="#fff" stroke-width="1"/></svg>
        www.verdanttablewellness.com
      </div>
      <div class="contact__social"></div>
    </div>
  </div>

  <footer class="cta">
    <strong>Call</strong> or <strong>email</strong> me today to schedule a <strong>free</strong><br>30-minute consultation.
  </footer>
</section>

<section class="flyer flyer--photo">
  <div class="top-rule"></div>
  <div class="hero-photo" role="img" aria-label="Photo of hands holding a glass salad bowl with tomatoes and peppers over a wooden cutting board"></div>
  <header class="brand">
    <div class="brand__text">
      <div class="brand__name">Verdant Table Wellness</div>
      <div class="brand__tagline">Nutrition Designs | Personal Chef Services</div>
    </div>
    <div class="brand__dot"></div>
  </header>
  <footer class="web-band">www.verdanttablewellness.com</footer>
</section>

</body>
</html>
```